San Francisco Hotel in need of banner ad set

We need a banner ad set for our new hotel in San Francisco called 'The Marigold Crestview'. The Marigold Crestview is joining our 'Bluewren Lodgings' portfolio of hotels. The final design should communicate 'Now a Piece of Bluewren Lodgings' and our introductory 15% discount.

Here are the details of the promotion:

http://mari.preview.tolvanek.com/promotions/welcome-to-bluewren-lodgings.htm

Ads are fixed (no flash, no animation)

Ad Dimensions:
120x120
160x600
300x250
728x90

Target Market(s)

Customers who have researched rates on our website and plan to travel to San Francisco. These ads will remarket our hotel to them after leaving our site.

Industry/Entity Type

Hotel

Font styles to use
Serif

Colors
ec1f27
faee3f

Requirements
Must have
• Check Availability button
The Marigold Crestview logo (attached both black and white depending on what you need)
Bluewren Lodgings logo
15% Off

Sub text:
No up front charges
24 hour cancellations
Nice to have
• No up front charges
24 hour cancellations

```html
<!DOCTYPE html>
<html lang="en">
<head>
<meta charset="utf-8">
<title>The Marigold Crestview – 15% Off Banner</title>
<link rel="stylesheet" href="https://fonts.googleapis.com/css2?family=Playfair+Display:wght@600;700&family=Source+Sans+3:wght@400;600&display=swap">
<style>
  :root {
    --brand-red: #ec1f27;
    --brand-yellow: #faee3f;
    --sky-deep: #3f6fd0;
    --sky-mid: #5b8ae4;
    --sky-light: #8fb3f0;
    --dusk-violet: #6b6fb8;
    --bridge-orange: #d5603a;
    --building-stone: #b9ad95;
    --building-shade: #6f6a5e;
    --white: #ffffff;
  }
  * { box-sizing: border-box; margin: 0; padding: 0; }
  html, body { width: 1200px; height: 148px; overflow: hidden; background: var(--white); }

  .banner {
    position: relative;
    width: 1200px;
    height: 148px;
    overflow: hidden;
    background: linear-gradient(90deg, var(--sky-deep) 0%, var(--sky-mid) 40%, var(--sky-light) 62%, var(--sky-mid) 80%, var(--sky-deep) 100%);
    font-family: "Source Sans 3", Arial, sans-serif;
  }

  .photo-bridge {
    position: absolute;
    left: 0; top: 0;
    width: 300px; height: 148px;
    background: linear-gradient(180deg, var(--dusk-violet) 0%, #8a7cc0 45%, var(--bridge-orange) 100%);
    -webkit-mask-image: linear-gradient(90deg, #000 70%, transparent 100%);
            mask-image: linear-gradient(90deg, #000 70%, transparent 100%);
  }

  .photo-hotel {
    position: absolute;
    right: 0; top: 0;
    width: 275px; height: 148px;
    background: linear-gradient(100deg, var(--building-shade) 0%, var(--building-stone) 45%, #d8cfbd 70%, var(--building-shade) 100%);
    -webkit-mask-image: linear-gradient(90deg, transparent 0%, #000 22%);
            mask-image: linear-gradient(90deg, transparent 0%, #000 22%);
  }

  .headline {
    position: absolute;
    left: 210px; top: 18px;
    width: 560px;
    text-align: center;
    font-family: "Playfair Display", Georgia, serif;
    font-weight: 700;
    font-size: 38px;
    letter-spacing: 0.5px;
    color: var(--white);
    text-shadow: 2px 2px 0 var(--brand-red);
    white-space: nowrap;
  }

  .cta-button {
    position: absolute;
    left: 218px; top: 80px;
    width: 140px; height: 31px;
    border-radius: 16px;
    background: var(--white);
    border: 1.5px solid var(--brand-red);
    color: var(--brand-red);
    font-size: 12.5px;
    font-weight: 600;
    letter-spacing: 0.6px;
    display: flex; align-items: center; justify-content: center;
    box-shadow: 0 2px 4px rgba(0,0,0,0.25);
  }

  .offer-terms {
    position: absolute;
    left: 374px; top: 87px;
    color: var(--brand-yellow);
    font-size: 13px;
    white-space: nowrap;
  }

  .discount-badge {
    position: absolute;
    left: 898px; top: 18px;
    width: 152px; height: 152px;
  }
  .discount-badge text {
    font-family: "Source Sans 3", Arial, sans-serif;
    font-weight: 600;
    fill: var(--brand-red);
  }

  .portfolio-mark {
    position: absolute;
    left: 1026px; top: 6px;
    width: 64px; height: 64px;
    border-radius: 50%;
    background: var(--white);
    display: flex; align-items: center; justify-content: center;
    text-align: center;
    font-family: "Playfair Display", Georgia, serif;
    font-weight: 600;
    font-size: 9px;
    line-height: 1.15;
    color: var(--building-shade);
  }
</style>
</head>
<body>
  <div class="banner">
    <div class="photo-bridge" role="img" aria-label="Golden Gate Bridge at dusk"></div>
    <div class="photo-hotel" role="img" aria-label="Exterior of The Marigold Crestview hotel building"></div>

    <h1 class="headline">THE MARIGOLD CRESTVIEW</h1>

    <div class="cta-button">CHECK AVAILABILITY</div>
    <p class="offer-terms">No upfront cost • 24-hour cancellation policy</p>

    <svg class="discount-badge" viewBox="0 0 152 152" aria-label="15% off">
      <circle cx="76" cy="76" r="74" fill="var(--brand-red)"/>
      <circle cx="76" cy="76" r="62" fill="var(--white)"/>
      <text x="76" y="72" text-anchor="middle" font-size="38">15%</text>
      <text x="76" y="108" text-anchor="middle" font-size="34">OFF</text>
    </svg>

    <div class="portfolio-mark">Bluewren<br>Lodgings</div>
  </div>
</body>
</html>
```